Finch Haulage Ltd

We need an A5 size (UK size) flyer to advertise our new business which is called Finch Haulage.
Domestic and Commercial Waste Clearance Services.
Please have the question in bold "Do you have a pile of junk you need to dispose of?"
We collect all kinds of junk or rubbish from homes and businesses across Kent, Sussex and South London.
No fuss, no mess!
A low cost, hassle free alternative to skip hire.
Licensed by the Landcare Board and fully insured (this can be in small print at the bottom).
Please put the Recycle symbol somewhere.
Our tagline on our vehicle is "We Clear More, For Less!"
We'd like the flyer to be bold and eye-catching (to catch the eye of the homeowner or business owner while it's sitting on their doormat).
We need our telephone, website and email to be prominent. Maybe saying "Call today for a free quote"
Tel. 01734 586019
Email: info@finchhaulage.example.co.uk
www.finchhaulage.example.co.uk
Target Market(s)
Our market will be homes and small businesses around Kent, Sussex and South London.

```html
<!DOCTYPE html>
<html lang="en">
<head>
<meta charset="utf-8">
<title>Finch Haulage – Waste Clearance Flyer</title>
<link rel="stylesheet" href="https://fonts.googleapis.com/css2?family=Open+Sans:wght@400;600;700&family=Roboto+Condensed:wght@700&display=swap">
<style>
  :root {
    --green-bright: #3cb44b;
    --green-mid: #2a9a3c;
    --green-dark: #17783a;
    --green-deep: #0f6a30;
    --green-pale: #b7e08a;
    --ink: #1c1c1c;
    --grey: #58595b;
    --white: #ffffff;
    --paper: #f4f4f4;
  }
  * { box-sizing: border-box; margin: 0; padding: 0; }
  html, body { width: 932px; height: 1200px; overflow: hidden; background: var(--white); }
  .flyer {
    position: relative; width: 932px; height: 1200px; overflow: hidden;
    font-family: "Open Sans", Arial, sans-serif; color: var(--white);
  }
  .condensed { font-family: "Roboto Condensed", "Arial Narrow", sans-serif; font-weight: 700; }

  /* Header */
  .header {
    position: absolute; left: 0; top: 0; width: 932px; height: 296px;
    background: linear-gradient(180deg, var(--white) 0%, var(--paper) 100%);
  }
  .brand {
    position: absolute; left: 70px; top: 110px; display: flex; align-items: center; gap: 16px;
  }
  .brand-dot { width: 34px; height: 34px; border-radius: 50%; background: var(--green-bright); }
  .brand-name { font-size: 52px; color: var(--grey); letter-spacing: 1px; }
  .question {
    position: absolute; left: 505px; top: 48px; width: 410px;
    font-size: 41px; line-height: 1.2; color: #333;
  }
  .url-tab {
    position: absolute; left: 420px; top: 246px; width: 430px; height: 50px;
    background: var(--green-mid);
    clip-path: polygon(5% 0, 95% 0, 100% 100%, 0 100%);
    display: flex; align-items: center; justify-content: center;
    font-size: 22px; letter-spacing: 0.5px;
  }

  /* Tagline band */
  .tagline-band {
    position: absolute; left: 0; top: 296px; width: 932px; height: 128px;
    background: linear-gradient(180deg, var(--green-bright), var(--green-mid));
    display: flex; align-items: center; justify-content: center;
  }
  .tagline { font-size: 66px; text-shadow: 0 3px 4px rgba(0,0,0,0.3); }

  /* Services panel */
  .services {
    position: absolute; left: 0; top: 424px; width: 932px; height: 449px;
    background: var(--green-dark); text-align: center;
    box-shadow: 0 6px 10px rgba(0,0,0,0.35);
  }
  .services-title { margin-top: 32px; font-size: 36px; }
  .services-area { margin-top: 2px; font-size: 27px; }
  .photo {
    position: absolute; top: 124px; width: 408px; height: 231px; border-radius: 10px;
  }
  .photo-commercial { left: 51px; background: linear-gradient(160deg, #c9b8a4, #8a7f78 55%, #5a5f6a); }
  .photo-domestic { left: 473px; background: linear-gradient(160deg, #b4563b, #7b6a5e 50%, #2e3a66); }
  .photo-label {
    position: absolute; bottom: 6px; font-size: 16px; color: var(--white);
    text-shadow: 0 1px 2px rgba(0,0,0,0.7);
  }
  .photo-commercial .photo-label { left: 20px; }
  .photo-domestic .photo-label { right: 16px; }
  .services-copy {
    position: absolute; left: 0; top: 374px; width: 932px;
    font-size: 21px; font-weight: 600; line-height: 1.45;
  }

  /* Call to action */
  .cta {
    position: absolute; left: 0; top: 873px; width: 932px; height: 274px;
    background: radial-gradient(circle at 80% 45%, #6fcf57 0%, var(--green-bright) 40%, var(--green-mid) 100%);
  }
  .cta-heading {
    position: absolute; left: 50px; top: 22px;
    font-family: "Open Sans", Arial, sans-serif; font-weight: 700;
    font-size: 42px; line-height: 1.25; color: var(--ink); letter-spacing: -1px;
  }
  .contact { position: absolute; left: 50px; display: flex; align-items: center; gap: 14px; }
  .contact-phone { top: 162px; font-size: 52px; }
  .contact-email { top: 222px; font-size: 31px; }
  .contact-icon { width: 40px; height: 40px; }
  .contact-email .contact-icon { width: 32px; height: 32px; }
  .contact-text { text-shadow: 0 2px 3px rgba(0,0,0,0.35); letter-spacing: 0.5px; }
  .recycle-ring {
    position: absolute; left: 606px; top: 6px; width: 228px; height: 228px; border-radius: 50%;
    border: 8px solid var(--green-pale); background: rgba(255,255,255,0.25);
  }
  .recycle-mark {
    position: absolute; left: 20px; top: 20px; width: 172px; height: 172px; border-radius: 50%;
    background: radial-gradient(circle at 40% 35%, #ffffff 0%, #e6f5d2 55%, #9fd36c 100%);
  }

  /* Footer */
  .footer {
    position: absolute; left: 0; top: 1147px; width: 932px; height: 53px;
    background: linear-gradient(90deg, var(--green-pale) 0%, #e3f2c9 45%, var(--white) 70%);
    display: flex; align-items: center; justify-content: space-between; padding: 0 24px 0 40px;
  }
  .licence { font-size: 14px; color: var(--ink); font-weight: 600; }
  .footer-url { font-size: 30px; color: var(--ink); }
</style>
</head>
<body>
<main class="flyer">
  <header class="header">
    <div class="brand">
      <span class="brand-dot"></span>
      <span class="brand-name condensed">Finch Haulage</span>
    </div>
    <h1 class="question condensed">Do you have a pile of junk you need to dispose of?</h1>
    <div class="url-tab condensed">www.finchhaulage.example.co.uk</div>
  </header>

  <section class="tagline-band">
    <h2 class="tagline condensed">We Clear More, For Less!</h2>
  </section>

  <section class="services">
    <h3 class="services-title condensed">Commercial Waste Clearance Services</h3>
    <p class="services-area condensed">across Kent, Sussex and South London.</p>
    <div class="photo photo-commercial" role="img" aria-label="Photo of a busy shopping centre interior">
      <span class="photo-label">Commercial</span>
    </div>
    <div class="photo photo-domestic" role="img" aria-label="Photo of an old sofa and television dumped against a brick wall">
      <span class="photo-label">Domestic</span>
    </div>
    <p class="services-copy">We collect all kinds of junk or rubbish from homes and business.<br>No fuss, no mess! Very competitive prices.</p>
  </section>

  <section class="cta">
    <p class="cta-heading">Call us today<br>for a FREE QUOTE"</p>
    <div class="contact contact-phone condensed">
      <svg class="contact-icon" viewBox="0 0 40 40" aria-hidden="true">
        <circle cx="20" cy="20" r="19" fill="#ffffff" opacity="0.9"/>
        <path d="M13 10c1-1 3-1 4 0l2 4c0 1 0 2-1 3l-1 1c1 3 3 5 6 6l1-1c1-1 2-1 3-1l4 2c1 1 1 3 0 4l-2 2c-2 1-6 0-10-4s-6-9-5-11z" fill="#3d6fa8"/>
      </svg>
      <span class="contact-text">01734 586019</span>
    </div>
    <div class="contact contact-email condensed">
      <svg class="contact-icon" viewBox="0 0 32 32" aria-hidden="true">
        <rect x="2" y="6" width="28" height="20" rx="3" fill="#ffffff"/>
        <path d="M3 8l13 10 13-10" fill="none" stroke="#3d6fa8" stroke-width="2.5"/>
      </svg>
      <span class="contact-text">info@finchhaulage.example.co.uk</span>
    </div>
    <div class="recycle-ring">
      <div class="recycle-mark" role="img" aria-label="Green recycling symbol"></div>
    </div>
  </section>

  <footer class="footer">
    <span class="licence">Licensed by the Landcare Board and fully insured</span>
    <span class="footer-url condensed">www.finchhaulage.example.co.uk</span>
  </footer>
</main>
</body>
</html>
```